Bref créative
Business Cards and Letterhead
85 mm x 55 mm / DIN A4 210 mm × 297 mm
Professional
Dominik R. Hartl
Lindenweg 7, 14471 Potsdam
info@lbr-planung.example
www.lbr-planung.example
Please use the standard german sizes for business cards and letters:
85 mm x 55 mm
DIN A4: 210 mm × 297 mm

```html
<!DOCTYPE html>
<html lang="de">
<head>
<meta charset="utf-8">
<title>lbrplanung – Geschäftsausstattung</title>
<link href="https://fonts.googleapis.com/css2?family=Roboto:wght@400;700;900&display=swap" rel="stylesheet">
<style>
:root{
  --orange:#f7963a;
  --ink:#2b2b2b;
  --grey:#6d6d6d;
  --paper:#ffffff;
  --black:#141414;
  --stage:#d9d9d9;
}
*{box-sizing:border-box;margin:0;padding:0}
html,body{width:1200px;height:629px;overflow:hidden}
body{background:var(--stage);font-family:"Roboto",Arial,sans-serif;color:var(--ink);position:relative}
.card,.sheet{position:absolute;background:var(--paper);box-shadow:0 2px 6px rgba(0,0,0,.25);overflow:hidden}
.card{width:144px;height:93px}
.brand{display:flex;align-items:center;gap:4px;font-weight:900;color:var(--ink);letter-spacing:-.2px;line-height:1}
.brand .mark{width:8px;height:8px;background:var(--orange)}
.brand.on-dark{color:var(--paper)}
.tagline{font-size:4px;color:var(--grey);margin-top:2px}
.card .brand{font-size:13px}
.name-bar{background:var(--orange);color:var(--paper);font-size:6px;font-weight:700;padding:4px 8px;height:16px}
.contact{font-size:4.5px;line-height:1.45;color:var(--grey)}
.card-front-a{left:84px;top:137px}
.card-front-a .body,.card-front-b .body{display:flex;gap:8px;padding:8px}
.card-back-white{left:245px;top:137px;display:flex;align-items:center;justify-content:center;flex-direction:column}
.card-back-orange{left:175px;top:252px;background:var(--orange);display:flex;align-items:center;justify-content:center;flex-direction:column}
.card-back-orange .tagline{color:var(--ink)}
.card-front-b{left:84px;top:360px}
.card-back-black{left:250px;top:360px;background:var(--black);display:flex;align-items:center;justify-content:center;flex-direction:column}
.card-back-black .tagline{color:#bbb}
.sheet{width:360px;height:512px;top:40px}
.sheet-first{left:439px}
.sheet-follow{left:802px}
.sheet .head-band{height:24px;background:var(--orange)}
.sheet .foot-band{position:absolute;left:0;right:0;bottom:0;height:18px;background:var(--orange);color:var(--paper);font-size:7px;text-align:center;line-height:18px;letter-spacing:.5px}
.letter-brand{position:absolute;left:14px;top:36px}
.letter-brand .brand{font-size:22px}
.letter-brand .brand .mark{width:12px;height:12px}
.letter-brand .tagline{font-size:5px}
.sender{position:absolute;left:164px;top:38px;font-size:4.5px;line-height:1.5;color:var(--grey)}
</style>
</head>
<body>

<div class="card card-front-a">
  <div class="name-bar">Dominik R. Hartl</div>
  <div class="body">
    <div>
      <div class="brand"><span class="mark"></span>lbrplanung</div>
      <div class="tagline">Planung und Beratung für Bauprojekte</div>
    </div>
    <div class="contact">Lindenweg 7<br>14471 Potsdam<br>Tel +49 331 555 0170<br>info@lbr-planung.example</div>
  </div>
</div>

<div class="card card-back-white">
  <div class="brand"><span class="mark"></span>lbrplanung</div>
  <div class="tagline">Planung und Beratung für Bauprojekte</div>
</div>

<div class="card card-back-orange">
  <div class="brand"><span class="mark" style="background:var(--paper)"></span>lbrplanung</div>
  <div class="tagline">Planung und Beratung für Bauprojekte</div>
</div>

<div class="card card-front-b">
  <div class="name-bar">Dominik R. Hartl</div>
  <div class="body">
    <div>
      <div class="brand"><span class="mark"></span>lbrplanung</div>
      <div class="tagline">Planung und Beratung für Bauprojekte</div>
    </div>
    <div class="contact">Lindenweg 7<br>14471 Potsdam<br>Tel +49 331 555 0170<br>info@lbr-planung.example</div>
  </div>
</div>

<div class="card card-back-black">
  <div class="brand on-dark"><span class="mark"></span>lbrplanung</div>
  <div class="tagline">Planung und Beratung für Bauprojekte</div>
</div>

<div class="sheet sheet-first">
  <div class="head-band"></div>
  <div class="letter-brand">
    <div class="brand"><span class="mark"></span>lbrplanung</div>
    <div class="tagline">Planung und Beratung für Bauprojekte</div>
  </div>
  <div class="sender">Lindenweg 7<br>14471 Potsdam<br><br>Tel +49 331 555 0170<br>Fax +49 331 555 0171<br><br>info@lbr-planung.example</div>
  <div class="foot-band">www.lbr-planung.example</div>
</div>

<div class="sheet sheet-follow">
  <div class="head-band"></div>
  <div class="foot-band">www.lbr-planung.example</div>
</div>

</body>
</html>
```